" Ajudamos funcionários expatriados de grandes empresas a encontrarem residência no Rio de janeiro. Ajudamos a instalar servicos essenciais na residencia e a fazer manutençào residencial "

```html
<!DOCTYPE html>
<html lang="pt-BR">
<head>
<meta charset="utf-8">
<title>clearnest – cartão de visita</title>
<link rel="stylesheet" href="https://fonts.googleapis.com/css2?family=Montserrat:wght@300;400;600;700&display=swap">
<style>
  :root {
    --page-bg: #ececec;
    --card-light: #ffffff;
    --card-light-end: #e6e7ea;
    --blue-deep: #2c4a87;
    --blue-mid: #4565a6;
    --blue-soft: #6f86bd;
    --lavender: #a9b3d6;
    --text-grey: #6a6a6a;
    --white: #ffffff;
  }
  * { box-sizing: border-box; margin: 0; padding: 0; }
  html, body { width: 1200px; height: 1200px; overflow: hidden; }
  body {
    background: var(--page-bg);
    font-family: "Montserrat", sans-serif;
    position: relative;
  }
  .card {
    position: absolute;
    left: 168px;
    width: 870px;
    height: 485px;
    overflow: hidden;
  }
  /* Front */
  .card-front {
    top: 72px;
    background: linear-gradient(160deg, var(--card-light) 30%, var(--card-light-end) 100%);
  }
  .front-skyline {
    position: absolute; left: 192px; top: 84px; width: 456px; height: 150px;
    background: linear-gradient(180deg, rgba(169,179,214,0.15) 0%, rgba(169,179,214,0.75) 100%);
  }
  .front-backdrop {
    position: absolute; left: 0; right: 0; top: 230px; height: 190px;
    background: linear-gradient(180deg, rgba(220,222,230,0) 0%, rgba(214,217,226,0.6) 100%);
  }
  .front-brand {
    position: absolute; left: 0; right: 0; top: 188px;
    text-align: center;
    font-size: 88px; font-weight: 400; letter-spacing: -1px;
    color: var(--blue-mid); line-height: 1;
  }
  .front-services {
    position: absolute; left: 0; right: 0; top: 298px;
    text-align: center; color: var(--text-grey);
    font-size: 20px; line-height: 26px;
  }
  .front-tagline {
    position: absolute; left: 0; right: 0; top: 374px;
    text-align: center; color: var(--blue-mid); font-size: 20px;
  }
  .front-rule { position: absolute; left: 0; width: 100%; height: 3px; background: var(--blue-soft); top: 430px; }
  .front-band {
    position: absolute; left: 0; bottom: 0; width: 100%; height: 42px;
    background: linear-gradient(90deg, var(--blue-mid), var(--blue-deep));
  }
  /* Back */
  .card-back {
    top: 641px;
    background: linear-gradient(135deg, var(--blue-mid) 0%, var(--blue-deep) 100%);
    color: var(--white);
  }
  .back-city {
    position: absolute; left: 0; right: 0; bottom: 0; height: 170px;
    background: linear-gradient(180deg, rgba(255,255,255,0) 0%, rgba(255,255,255,0.12) 100%);
  }
  .back-skyline {
    position: absolute; left: 96px; top: 127px; width: 252px; height: 96px;
    background: linear-gradient(180deg, rgba(255,255,255,0.1) 0%, rgba(200,210,240,0.55) 100%);
  }
  .back-brand {
    position: absolute; left: 70px; width: 300px; top: 216px;
    text-align: center;
    font-size: 60px; font-weight: 400; letter-spacing: -1px; line-height: 1;
  }
  .back-subtitle {
    position: absolute; left: 70px; width: 300px; top: 298px;
    text-align: center; font-size: 18px; font-weight: 300;
  }
  .back-divider { position: absolute; left: 389px; top: 43px; width: 2px; height: 372px; background: rgba(255,255,255,0.7); }
  .person-name { position: absolute; left: 422px; top: 48px; font-size: 28px; font-weight: 600; }
  .person-role { position: absolute; left: 422px; top: 86px; font-size: 22px; font-weight: 600; }
  .contact-list { position: absolute; left: 420px; top: 0; list-style: none; }
  .contact-item { position: absolute; left: 0; display: flex; align-items: flex-start; gap: 14px; width: 430px; }
  .contact-icon { flex: 0 0 34px; width: 34px; height: 34px; }
  .contact-text { font-size: 17px; font-weight: 600; line-height: 22px; padding-top: 5px; white-space: nowrap; }
</style>
</head>
<body>

<section class="card card-front">
  <div class="front-backdrop" role="img" aria-label="Faint city buildings illustration"></div>
  <div class="front-skyline" role="img" aria-label="City skyline illustration"></div>
  <div class="front-brand">clearnest</div>
  <p class="front-services">Look and See - Housing Hunting - Settle-in services - Ongoing Support<br>Property return negotiation - Customized Services</p>
  <p class="front-tagline">Things can be easier for you</p>
  <div class="front-rule"></div>
  <div class="front-band"></div>
</section>

<section class="card card-back">
  <div class="back-city" role="img" aria-label="Faint city buildings illustration"></div>
  <div class="back-skyline" role="img" aria-label="City skyline illustration"></div>
  <div class="back-brand">clearnest</div>
  <p class="back-subtitle">Relocation Solutions</p>
  <div class="back-divider"></div>

  <h1 class="person-name">Lívia Tavares</h1>
  <p class="person-role">Co-Founder</p>

  <ul class="contact-list">
    <li class="contact-item" style="top:149px">
      <svg class="contact-icon" viewBox="0 0 34 34"><circle cx="17" cy="17" r="16" fill="rgba(255,255,255,0.25)"/><path d="M12 10 l3 0 l1.5 4 l-2 1.5 a9 9 0 0 0 4 4 l1.5-2 l4 1.5 l0 3 a2 2 0 0 1-2 2 a13 13 0 0 1-12-12 a2 2 0 0 1 2-2z" fill="#fff"/></svg>
      <span class="contact-text">+55 (21) 90412 5577</span>
    </li>
    <li class="contact-item" style="top:205px">
      <svg class="contact-icon" viewBox="0 0 34 34"><circle cx="17" cy="17" r="16" fill="rgba(255,255,255,0.25)"/><path d="M17 8 a6 6 0 0 1 6 6 c0 5-6 12-6 12 s-6-7-6-12 a6 6 0 0 1 6-6z" fill="#fff"/><circle cx="17" cy="14" r="2.2" fill="#3a5a98"/></svg>
      <span class="contact-text">Rua das Palmeiras, 1280<br>4º andar – Bloco 2, Sala 105<br>Barra da Tijuca, Rio de Janeiro -RJ<br>CEP - 22640-100</span>
    </li>
    <li class="contact-item" style="top:297px">
      <svg class="contact-icon" viewBox="0 0 34 34"><circle cx="17" cy="17" r="16" fill="rgba(255,255,255,0.25)"/><rect x="9" y="11" width="16" height="12" rx="1.5" fill="#fff"/><path d="M9.5 12 l7.5 6 l7.5-6" fill="none" stroke="#3a5a98" stroke-width="1.5"/></svg>
      <span class="contact-text">livia@clearnest.com.br</span>
    </li>
    <li class="contact-item" style="top:350px">
      <svg class="contact-icon" viewBox="0 0 34 34"><circle cx="17" cy="17" r="16" fill="rgba(255,255,255,0.25)"/><circle cx="17" cy="17" r="8" fill="none" stroke="#fff" stroke-width="1.6"/><path d="M9 17 h16 M17 9 c-4 4-4 12 0 16 M17 9 c4 4 4 12 0 16" fill="none" stroke="#fff" stroke-width="1.4"/></svg>
      <span class="contact-text">www.clearnest.com.br</span>
    </li>
  </ul>
</section>

</body>
</html>
```